Architectural, Engineering and Design Build

Tavonex4.com
Veteran Disabled Certified company is doing business in Architecture, Engineer and Design build - look simialr websites and come up with design follow following website
https://dorsey-kalbin.example/
https://www.velmonteam.example/
https://www.pirnoqa.example/contract-vehicles/service-disabled-veteran-owned-small-business-sdvosb/
https://www.corbelhubnet.example/about/sdvosb/

Target Market(s)

US - Defense and Federal Government

Industry/Entity Type

Colors
0054AA
0677BA
7BADD7
CADEEF
E8F1F8

Requirements
Must have
• Army, American patriotism , Buildings, construction, architecture, engineering
Nice to have
• I need to attract federal government agencies and Defense

```html
<!DOCTYPE html>
<html lang="en">
<head>
<meta charset="utf-8">
<title>Tavonex4 — Construction Management &amp; Engineering Design</title>
<link href="https://fonts.googleapis.com/css2?family=Josefin+Sans:wght@600;700&family=Exo+2:wght@600;700&family=Lato:wght@400;700&display=swap" rel="stylesheet">
<style>
:root{
  --navy:#1b2a6b;
  --blue:#0054aa;
  --blue-mid:#0677ba;
  --blue-soft:#7badd7;
  --blue-pale:#cadeef;
  --blue-wash:#e8f1f8;
  --red:#d7262c;
  --ink:#1d1d1f;
  --text:#4a4a4f;
  --grey-bg:#f1f1f2;
  --white:#fff;
}
*{box-sizing:border-box;margin:0;padding:0}
html,body{width:1200px;height:4886px;overflow:hidden}
body{position:relative;background:var(--white);font-family:"Lato",sans-serif;color:var(--text)}
.abs{position:absolute}
.btn{position:absolute;display:flex;align-items:center;justify-content:center;color:var(--white);font-size:12px;font-family:"Lato",sans-serif}
.btn--navy{background:var(--navy);border-radius:22px}
.btn--blue{background:var(--blue)}
.section-title{position:absolute;left:0;width:1200px;text-align:center;font-family:"Exo 2",sans-serif;font-weight:700;font-size:31px;color:var(--ink);text-transform:uppercase}
.section-title::after{content:"";display:block;width:56px;height:3px;background:var(--red);margin:8px auto 0}
.photo{position:absolute}
.brand-word{font-family:"Exo 2",sans-serif;font-weight:700;letter-spacing:1px}
.topbar{left:388px;top:0;width:670px;height:34px;background:var(--blue);border-radius:0 0 0 18px;color:var(--white);font-size:12px;display:flex;align-items:center;padding-left:28px;gap:30px}
.topbar .social{margin-left:auto;display:flex}
.topbar .social span{width:36px;height:34px;border-left:1px solid rgba(255,255,255,.35);display:flex;align-items:center;justify-content:center}
.topbar .social i{width:10px;height:10px;border:1.5px solid var(--white);border-radius:50%}
.nav{top:66px;left:408px;font-size:13px;color:var(--ink)}
.nav a{position:absolute;white-space:nowrap;text-decoration:none;color:var(--ink)}
.nav a.active{color:var(--blue)}
.nav a.active::after{content:"";display:block;height:2px;background:var(--blue);margin-top:4px}
.hero-title{left:140px;top:232px;font-family:"Josefin Sans",sans-serif;font-weight:700;font-size:39px;line-height:49px;color:var(--ink);letter-spacing:.5px}
.about-title{left:648px;top:748px;font-family:"Exo 2",sans-serif;font-weight:700;font-size:29px;color:var(--ink)}
.about-title::after{content:"";display:block;width:56px;height:3px;background:var(--red);margin-top:4px}
.body-copy{font-size:11.5px;line-height:23px;color:var(--text)}
.card{position:absolute;background:var(--white);border-radius:14px;box-shadow:0 2px 10px rgba(0,0,0,.06)}
.card h3{font-family:"Lato",sans-serif;font-weight:700;font-size:15px;color:var(--ink);text-align:center}
.card p{font-size:11.5px;line-height:20px;text-align:center;color:var(--text)}
.round-arrow{position:absolute;width:30px;height:30px;border-radius:50%;background:var(--navy);display:flex;align-items:center;justify-content:center}
.badge{position:absolute;background:var(--white);border-radius:6px;box-shadow:0 2px 10px rgba(0,0,0,.08);display:flex;align-items:center;justify-content:center}
.gallery-cap h3{font-family:"Lato",sans-serif;font-weight:700;font-size:15.5px;line-height:22px;color:var(--ink)}
.why-card{position:absolute;background:var(--white);box-shadow:0 3px 14px rgba(0,0,0,.08);text-align:center}
.why-card h3{font-weight:700;font-size:14px;line-height:21px;color:var(--ink)}
.why-card p{font-size:11.5px;line-height:20px;margin-top:10px}
.why-icon{position:absolute;left:50%;top:-48px;margin-left:-48px;width:96px;height:96px}
.quote{position:absolute;background:var(--white);box-shadow:0 3px 14px rgba(0,0,0,.08)}
.quote .who{position:absolute;left:95px;top:20px;font-weight:700;font-size:15px;color:var(--ink)}
.quote .stars{position:absolute;left:95px;top:42px;color:#f5b400;font-size:13px;letter-spacing:2px}
.quote .avatar{position:absolute;left:-12px;top:-10px;width:92px;height:88px;background:linear-gradient(160deg,#8b8a6a,#4d4a38)}
.quote .mark{position:absolute;right:28px;top:-8px;width:44px;height:68px;background:var(--red);clip-path:polygon(0 0,100% 0,100% 100%,50% 84%,0 100%)}
.quote p{position:absolute;left:40px;top:96px;width:340px;font-size:11.5px;line-height:23px}
.footer-h{position:absolute;top:4584px;font-family:"Lato",sans-serif;font-weight:700;font-size:15px;color:var(--white)}
.footer-h::after{content:"";display:block;width:28px;height:2px;background:var(--red);margin-top:8px}
.flist{position:absolute;color:var(--white);font-size:11.5px}
</style>
</head>
<body>

<div class="abs topbar">
  <span>&#9742;&nbsp; (555) 014-2286</span>
  <span>&#9993;&nbsp; tavonex4@mailbox.example</span>
  <div class="social"><span><i></i></span><span><i></i></span><span><i></i></span><span><i></i></span></div>
</div>

<div class="photo" role="img" aria-label="Hero photo: engineer in hard hat and safety vest reviewing plans with a manager at a construction site" style="left:0;top:0;width:1200px;height:635px;background:linear-gradient(90deg,#ffffff 0%,#f4f4f2 30%,#d9d6cf 55%,#b9a993 75%,#8e7d68 100%);z-index:-1"></div>

<div class="abs" style="left:142px;top:30px;display:flex;align-items:center;gap:10px">
  <span style="width:26px;height:26px;border-radius:50%;background:var(--navy)"></span>
  <span class="brand-word" style="font-size:26px;color:var(--navy)">TAVONEX4</span>
</div>

<nav class="abs nav">
  <a class="active" style="left:0">HOME</a>
  <a style="left:85px">ABOUT US</a>
  <a style="left:193px">SERVICES</a>
  <a style="left:299px">PROJECTS</a>
  <a style="left:407px">CAREERS</a>
</nav>
<div class="btn btn--blue" style="left:918px;top:57px;width:140px;height:34px;font-size:12px">CONTACT US</div>

<h1 class="abs hero-title">CONSTRUCTION<br>MANAGEMENT &amp;<br>ENGINEERING DESIGN</h1>
<div class="btn btn--blue" style="left:142px;top:400px;width:141px;height:34px">CONTACT US</div>

<svg class="abs" style="left:0;top:480px" width="1200" height="160" viewBox="0 0 1200 160">
  <path d="M0 30 C200 180 500 120 800 70 C1000 40 1120 80 1200 120 L1200 160 L0 160Z" fill="var(--white)"/>
  <path d="M0 30 C200 180 500 120 800 70 C1000 40 1120 80 1200 120" fill="none" stroke="var(--blue)" stroke-width="6"/>
  <path d="M0 40 C220 190 520 130 800 82 C1000 52 1120 92 1200 132" fill="none" stroke="var(--blue-pale)" stroke-width="4"/>
</svg>

<svg class="abs" style="left:137px;top:687px" width="420" height="420" viewBox="0 0 420 420">
  <circle cx="210" cy="210" r="206" fill="none" stroke="var(--red)" stroke-width="5" stroke-dasharray="650 1000" transform="rotate(150 210 210)"/>
  <circle cx="210" cy="210" r="206" fill="none" stroke="var(--navy)" stroke-width="5" stroke-dasharray="650 1000" transform="rotate(330 210 210)"/>
</svg>
<div class="photo" role="img" aria-label="Workers silhouetted on steel scaffolding at sunset" style="left:147px;top:697px;width:400px;height:400px;border-radius:50%;background:linear-gradient(180deg,#6c8fb3 0%,#c8a47a 55%,#3b3a3c 100%)"></div>

<h2 class="abs about-title">ABOUT TAVONEX4</h2>
<p class="abs body-copy" style="left:648px;top:810px;width:410px">Lorem ipsum dolor sit amet, consectetur adipiscing elit, sed do eiusmod ut tempor incididunt ut labore et dolore magna aliqua. Ut enim ad minim ex veniam, quis nostrud exercitation ullamco laboris nisi ut aliquip ex ea amet commodo consequat. Duis aute irure dolor in reprehenderit in voluptate velit esse cillum dolore eu fugiat nulla pariatur.</p>
<p class="abs body-copy" style="left:648px;top:930px;width:410px"><b style="color:var(--ink)">Our Mission</b> : Sed ut perspiciatis unde omnis iste natus error sit amet ex ea voluptatem accusantium doloremque laudantium.</p>
<div class="btn btn--navy" style="left:648px;top:1001px;width:126px;height:40px">Read More</div>
<div class="photo" role="img" aria-label="Faint decorative texture" style="left:975px;top:1016px;width:118px;height:40px;background:#f2f2f4;border-radius:3px"></div>

<section class="abs" style="left:0;top:1189px;width:1200px;height:618px;background:var(--grey-bg)"></section>
<h2 class="section-title" style="top:1266px">Our Services</h2>

<div class="card" style="left:142px;top:1340px;width:290px;height:366px">
  <div class="photo" role="img" aria-label="Hands drafting architectural blueprints with a pencil and magnifier" style="left:14px;top:14px;width:262px;height:244px;border-radius:10px;background:linear-gradient(135deg,#e9e6df,#b9b3a6)"></div>
  <h3 class="abs" style="left:0;top:276px;width:290px">Architectural</h3>
  <p class="abs" style="left:20px;top:300px;width:250px">Lorem ipsum dolor sit amet, consectetur adipiscing elit.</p>
</div>
<div class="card" style="left:455px;top:1340px;width:290px;height:366px">
  <div class="photo" role="img" aria-label="Engineer in hard hat and safety vest holding plans on site" style="left:14px;top:14px;width:262px;height:244px;border-radius:10px;background:linear-gradient(135deg,#cfd4d8,#7f8b72)"></div>
  <h3 class="abs" style="left:0;top:276px;width:290px">Engineering Work</h3>
  <p class="abs" style="left:20px;top:300px;width:250px">Lorem ipsum dolor sit amet, consectetur adipiscing elit.</p>
</div>
<div class="card" style="left:768px;top:1340px;width:290px;height:366px">
  <div class="photo" role="img" aria-label="Designer sketching building plans at a desk" style="left:14px;top:14px;width:262px;height:244px;border-radius:10px;background:linear-gradient(135deg,#6a7a52,#d6d3cb)"></div>
  <h3 class="abs" style="left:0;top:276px;width:290px">Design Build</h3>
  <p class="abs" style="left:20px;top:300px;width:250px">Lorem ipsum dolor sit amet, consectetur adipiscing elit.</p>
</div>
<div class="round-arrow" style="left:272px;top:1689px"><svg width="12" height="12" viewBox="0 0 12 12"><path d="M4 2l4 4-4 4" stroke="#fff" stroke-width="2" fill="none"/></svg></div>
<div class="round-arrow" style="left:585px;top:1689px"><svg width="12" height="12" viewBox="0 0 12 12"><path d="M4 2l4 4-4 4" stroke="#fff" stroke-width="2" fill="none"/></svg></div>
<div class="round-arrow" style="left:898px;top:1689px"><svg width="12" height="12" viewBox="0 0 12 12"><path d="M4 2l4 4-4 4" stroke="#fff" stroke-width="2" fill="none"/></svg></div>

<h2 class="abs" style="left:140px;top:1885px;font-family:'Exo 2',sans-serif;font-weight:700;font-size:31px;color:var(--ink)">KEY INDUSTRY CERTIFICATIONS</h2>
<div class="abs" style="left:142px;top:1928px;width:56px;height:3px;background:var(--red)"></div>
<p class="abs body-copy" style="left:142px;top:1934px;width:460px">Sed ut perspiciatis unde omnis iste natus error sit voluptatem accusantium amet doloremque laudantium, totam rem aperiam, eaque ipsa quae ab illo.</p>
<div class="btn btn--navy" style="left:142px;top:2006px;width:125px;height:38px">Contact Us</div>
<div class="badge" style="left:620px;top:1928px;width:133px;height:82px"><span style="width:90px;height:40px;border-radius:4px;background:var(--blue-pale)"></span></div>
<div class="badge" style="left:772px;top:1928px;width:133px;height:82px"><span style="width:90px;height:40px;border-radius:4px;background:#f4c9ca"></span></div>
<div class="badge" style="left:924px;top:1928px;width:134px;height:82px"><span style="width:60px;height:40px;border-radius:4px;background:var(--blue-pale)"></span></div>

<section class="abs" style="left:0;top:2131px;width:1200px;height:696px;background:var(--grey-bg)"></section>
<h2 class="section-title" style="top:2209px">Project Gallery</h2>
<p class="abs body-copy" style="left:0;top:2272px;width:1200px;text-align:center">Sed ut perspiciatis unde omnis iste natus error sit voluptatem accusantium doloremque laudantium, totam rem aperiam, eaque ipsa quae ab illo.</p>

<div class="photo" role="img" aria-label="Building under construction with a tower crane at golden hour" style="left:142px;top:2319px;width:440px;height:244px;border-radius:8px;background:linear-gradient(160deg,#3a6fb8 0%,#e5b04e 50%,#6b4a20 100%)"></div>
<div class="photo" role="img" aria-label="Classical government building facade with columns and flag" style="left:618px;top:2319px;width:440px;height:244px;border-radius:8px;background:linear-gradient(180deg,#b7cde0 0%,#8d8a82 45%,#4d4b47 100%)"></div>
<div class="abs gallery-cap" style="left:142px;top:2578px;width:440px"><h3>Lorem Ipsum Is Simply Dummy Text Of The Printing And Typesetting Industry.</h3><p class="body-copy" style="margin-top:8px">Sed ut perspiciatis unde omnis iste natus error sit voluptatem accusantium amet doloremque laudantium, totam rem aperiam, eaque ipsa quae ab illo.</p></div>
<div class="abs gallery-cap" style="left:618px;top:2578px;width:440px"><h3>Lorem Ipsum Is Simply Dummy Text Of The Printing And Typesetting Industry.</h3><p class="body-copy" style="margin-top:8px">Sed ut perspiciatis unde omnis iste natus error sit voluptatem accusantium amet doloremque laudantium, totam rem aperiam, eaque ipsa quae ab illo.</p></div>
<div class="btn btn--navy" style="left:512px;top:2704px;width:176px;height:38px">Explore More Projects</div>

<h2 class="section-title" style="top:2905px">Why Choose Us</h2>
<p class="abs body-copy" style="left:0;top:2968px;width:1200px;text-align:center">Lorem ipsum dolor sit amet, consectetur adipiscing elit, sed do eiusmod tempor incididunt ut labore et dolore magna aliqua.</p>

<div class="why-card" style="left:142px;top:3053px;width:282px;height:191px">
  <svg class="why-icon" viewBox="0 0 96 96"><path d="M10 60 A40 40 0 0 1 40 10" fill="none" stroke="var(--red)" stroke-width="2"/><path d="M86 36 A40 40 0 0 1 56 86" fill="none" stroke="var(--red)" stroke-width="2"/><circle cx="48" cy="48" r="34" fill="var(--navy)"/><g fill="none" stroke="#fff" stroke-width="2"><path d="M34 62V36h28v26M34 44h28M42 36v26M54 36v26"/></g></svg>
  <h3 style="margin-top:60px">Veteran-Owned<br>Business</h3>
  <p>Duis aute irure dolor in reprehenderit in<br>voluptate velit esse cillum dolore.</p>
</div>
<div class="why-card" style="left:459px;top:3053px;width:282px;height:191px">
  <svg class="why-icon" viewBox="0 0 96 96"><path d="M10 60 A40 40 0 0 1 40 10" fill="none" stroke="var(--red)" stroke-width="2"/><path d="M86 36 A40 40 0 0 1 56 86" fill="none" stroke="var(--red)" stroke-width="2"/><circle cx="48" cy="48" r="34" fill="var(--navy)"/><g fill="none" stroke="#fff" stroke-width="2"><circle cx="48" cy="42" r="8"/><path d="M34 64c2-10 26-10 28 0M38 36h20"/></g></svg>
  <h3 style="margin-top:60px">Experience and<br>Expertise</h3>
  <p>Duis aute irure dolor in reprehenderit in<br>voluptate velit esse cillum dolore.</p>
</div>
<div class="why-card" style="left:777px;top:3053px;width:281px;height:191px">
  <svg class="why-icon" viewBox="0 0 96 96"><path d="M10 60 A40 40 0 0 1 40 10" fill="none" stroke="var(--red)" stroke-width="2"/><path d="M86 36 A40 40 0 0 1 56 86" fill="none" stroke="var(--red)" stroke-width="2"/><circle cx="48" cy="48" r="34" fill="var(--navy)"/><g fill="none" stroke="#fff" stroke-width="2"><circle cx="48" cy="42" r="11"/><path d="M42 52l-4 14 10-5 10 5-4-14"/></g></svg>
  <h3 style="margin-top:60px">Commitment to<br>Quality</h3>
  <p>Duis aute irure dolor in reprehenderit in<br>voluptate velit esse cillum dolore.</p>
</div>

<section class="abs" style="left:0;top:3327px;width:1200px;height:598px;background:#f7f7f8"></section>
<div class="quote" style="left:154px;top:3417px;width:405px;height:195px">
  <div class="avatar photo" role="img" aria-label="Portrait photo of a client in military uniform"></div>
  <div class="who">Jane Smith</div><div class="stars">★★★★★</div>
  <div class="mark"></div>
  <p>Lorem ipsum dolor sit amet, consectetur adipiscing elit, sed do eiusmod tempor incididunt ut labore et dolore magna aliqua. Ut enim ad minim veniam, quis nostrud exercitation ullamco laboris nisi ut.</p>
</div>
<div class="quote" style="left:154px;top:3650px;width:405px;height:193px">
  <div class="avatar photo" role="img" aria-label="Portrait photo of a client in military uniform"></div>
  <div class="who">Emily Johnson</div><div class="stars">★★★★★</div>
  <div class="mark"></div>
  <p>Lorem ipsum dolor sit amet, consectetur adipiscing elit, sed do eiusmod tempor incididunt ut labore et dolore magna aliqua. Ut enim ad minim veniam, quis nostrud exercitation ullamco laboris nisi ut.</p>
</div>
<h2 class="abs" style="left:650px;top:3405px;font-family:'Exo 2',sans-serif;font-weight:700;font-size:29px;color:var(--ink)">WHAT ARE PEOPLE SAYING?</h2>
<div class="abs" style="left:650px;top:3446px;width:56px;height:3px;background:var(--red)"></div>
<p class="abs body-copy" style="left:650px;top:3468px;width:420px">Lorem Ipsum is simply dummy text of the printing and typesetting industry. Lorem Ipsum has been the industry's standard.</p>
<div class="abs" style="left:652px;top:3817px;width:34px;height:34px;border-radius:50%;border:1.5px solid var(--ink);display:flex;align-items:center;justify-content:center"><svg width="14" height="10" viewBox="0 0 14 10"><path d="M13 5H2M5 1L1 5l4 4" stroke="var(--ink)" stroke-width="1.8" fill="none"/></svg></div>
<div class="abs" style="left:701px;top:3817px;width:34px;height:34px;border-radius:50%;background:var(--navy);display:flex;align-items:center;justify-content:center"><svg width="14" height="10" viewBox="0 0 14 10"><path d="M1 5h11M9 1l4 4-4 4" stroke="#fff" stroke-width="1.8" fill="none"/></svg></div>

<div class="photo" role="img" aria-label="Red camouflage pattern background" style="left:142px;top:4010px;width:916px;height:362px;border-radius:22px;background:radial-gradient(circle at 30% 40%,#e1353a,#c41f25 60%,#a9171c)"></div>
<h2 class="abs" style="left:142px;top:4086px;width:916px;text-align:center;font-family:'Exo 2',sans-serif;font-weight:700;font-size:35px;line-height:44px;color:var(--white)">Lorem Ipsum Dolor Sit Amet, Consectetur<br>Adipiscing Elit</h2>
<p class="abs" style="left:270px;top:4188px;width:660px;text-align:center;font-size:13px;line-height:24px;color:var(--white)">Lorem Ipsum is simply dummy text &nbsp;printing and typesetting industry. Lorem Ipsum has been the industry's standard du ever since the 1500s, when an unknown printer took</p>
<div class="btn btn--navy" style="left:523px;top:4260px;width:154px;height:36px">Project Cosultation</div>

<svg class="abs" style="left:0;top:4440px" width="1200" height="446" viewBox="0 0 1200 446">
  <path d="M0 132 C300 20 700 -10 1200 70 L1200 446 L0 446Z" fill="var(--navy)"/>
  <path d="M0 132 C300 20 700 -10 1200 70" fill="none" stroke="var(--red)" stroke-width="8"/>
</svg>

<h4 class="footer-h" style="left:142px">Quick Links</h4>
<ul class="flist" style="left:142px;top:4630px;list-style:none;line-height:28px">
  <li>›&nbsp; Home</li><li>›&nbsp; About Us</li><li>›&nbsp; Services</li><li>›&nbsp; Projects</li><li>›&nbsp; Contact Us</li>
</ul>

<h4 class="footer-h" style="left:343px">Contact Details</h4>
<div class="flist" style="left:343px;top:4636px;line-height:18px">
  <div style="display:flex;gap:10px"><span>&#9679;</span><span>123, Building Name, Street<br>City, State XY 123456</span></div>
  <div style="display:flex;gap:10px;margin-top:12px"><span>&#9742;</span><span><b>Phone</b><br>123-456-7890</span></div>
  <div style="display:flex;gap:10px;margin-top:12px"><span>&#9993;</span><span><b>Email</b><br>info@tavonex4.example</span></div>
</div>

<h4 class="footer-h" style="left:647px">Follow Us</h4>
<ul class="flist" style="left:647px;top:4640px;list-style:none">
  <li style="display:flex;align-items:center;gap:12px;height:40px"><span style="width:24px;height:24px;border:1.5px solid #fff;border-radius:50%"></span>Folkboard</li>
  <li style="display:flex;align-items:center;gap:12px;height:40px"><span style="width:24px;height:24px;border:1.5px solid #fff;border-radius:50%"></span>Chirpline</li>
  <li style="display:flex;align-items:center;gap:12px;height:40px"><span style="width:24px;height:24px;border:1.5px solid #fff;border-radius:50%"></span>Viewcast</li>
  <li style="display:flex;align-items:center;gap:12px;height:40px"><span style="width:24px;height:24px;border:1.5px solid #fff;border-radius:50%"></span>Snapgrid</li>
</ul>

<div class="abs" style="left:853px;top:4680px;display:flex;align-items:center;gap:10px">
  <span style="width:26px;height:26px;border-radius:50%;background:var(--white)"></span>
  <span class="brand-word" style="font-size:30px;color:var(--white)">TAVONEX4</span>
</div>

<div class="abs" style="left:142px;top:4835px;width:916px;height:1px;background:rgba(255,255,255,.3)"></div>
<p class="abs" style="left:0;top:4855px;width:1200px;text-align:center;font-size:11px;color:var(--white)">© 2024 Tavonex4. All Rights Reserved</p>

</body>
</html>
```